Quarrybend Building Company / Website*

We need a design for a contracting company website based in KSA, something modern with the same color theme as the attached logo. including a page for people who want to submit their CV and try to apply for a job.Also to include the "about us, contact us, gallery, Divisions, Supplies, etc...". If possible to have an interactive or moving background. Please disregard the "Smart Solutions" Section in the attached profile.

Industry/Entity Type

Construction Company

Number of Pages Required

5+ page

Colors

Designer to choose colors to be used in the design.

Requirements
Must have
• Pages:
• about us, contact us, gallery, Divisions, Apply for a job, Supplies
Nice to have
• - Moving or interactive background

```html
<!DOCTYPE html>
<html lang="en">
<head>
<meta charset="utf-8">
<title>Quarrybend Building Company</title>
<link href="https://fonts.googleapis.com/css2?family=Poppins:wght@300;400;500;600;700&display=swap" rel="stylesheet">
<style>
:root{
  --brown:#3a2f26;
  --brown-dark:#2f261f;
  --yellow:#f5b021;
  --white:#ffffff;
  --paper:#f6f6f6;
  --ink:#2a2a2a;
  --muted:#8a8a8a;
  --line:#5a4d41;
}
*{margin:0;padding:0;box-sizing:border-box}
html,body{width:1200px;height:3571px;overflow:hidden}
body{position:relative;font-family:'Poppins',sans-serif;background:var(--brown);color:var(--white)}
.abs{position:absolute}
a{color:inherit;text-decoration:none}

/* header */
.site-header{left:0;top:0;width:1200px;height:83px;background:var(--brown)}
.brand{left:83px;top:14px;display:flex;align-items:center;gap:10px}
.brand-mark{width:34px;height:34px;background:var(--yellow)}
.brand-name{font-size:17px;font-weight:600;line-height:1.05;color:var(--white)}
.brand-name small{display:block;font-size:9px;font-weight:400;letter-spacing:.5px}
.main-nav{left:416px;top:32px;display:flex;gap:30px;font-size:11px;font-weight:600;text-transform:uppercase}
.main-nav .active{color:var(--yellow)}
.header-phone{left:875px;top:31px;font-size:13px;font-weight:600;display:flex;align-items:center;gap:6px}
.btn{display:inline-block;background:var(--yellow);color:var(--white);font-size:10px;font-weight:600;text-transform:uppercase;text-align:center}
.header-cta{left:1005px;top:22px;width:112px;height:38px;line-height:38px}

/* hero */
.hero{left:83px;top:83px;width:1117px;height:541px;background:linear-gradient(160deg,#8ea3bd 0%,#4d5e74 45%,#2a3442 100%)}
.hero-title{left:214px;top:330px;font-size:42px;font-weight:400;line-height:1.2}
.hero-title b{font-weight:700}
.hero-cta{left:214px;top:462px;width:114px;height:32px;line-height:32px}
.social-rail{left:30px;top:510px;display:flex;flex-direction:column;gap:14px}
.social-rail span{width:14px;height:14px;border:1.5px solid var(--white);border-radius:50%}

/* about */
.about-photo{left:214px;top:707px;width:310px;height:276px;background:linear-gradient(135deg,#d9d3c9,#8b6a52 60%,#5a4a3d)}
.about-body{left:610px;top:722px;width:380px}
.about-body h2{font-size:27px;font-weight:600;line-height:1.2}
.about-body h3{font-size:16px;font-weight:500;line-height:1.35;margin-top:18px}
.about-body p{font-size:11px;line-height:1.75;color:#d8d0c8;margin-top:18px}
.link-more{display:inline-block;margin-top:20px;font-size:10px;font-weight:600;color:var(--yellow);text-transform:uppercase}
.stat{top:1040px;display:flex;align-items:center;gap:14px}
.stat svg{width:105px;height:105px}
.stat .cap{font-size:9px;color:#d8d0c8}
.stat .name{font-size:19px;font-weight:600;line-height:1.2}
.stat .desc{font-size:10px;color:#d8d0c8;line-height:1.4}

/* services */
.services{left:0;top:1226px;width:1200px;height:493px;background:var(--paper);color:var(--ink)}
.section-title{font-size:26px;font-weight:600}
.view-all{font-size:10px;font-weight:600;text-transform:uppercase}
.service-card{top:167px;width:240px;height:250px;padding:0 0 0 0}
.service-card.featured{background:var(--yellow);color:var(--white);padding:20px 20px}
.service-card h4{font-size:17px;font-weight:600;margin-top:18px}
.service-card p{font-size:11px;line-height:1.75;color:var(--muted);margin-top:14px}
.service-card.featured p{color:var(--white)}
.service-card .read{display:block;font-size:9px;font-weight:600;text-transform:uppercase;margin-top:18px}
.arrow{font-size:16px;color:var(--ink)}

/* gallery */
.gallery-band{left:0;top:1719px;width:1200px;height:107px;background:var(--yellow)}
.gallery-band .section-title{color:var(--brown);position:absolute;left:214px;top:36px}
.filters{left:683px;top:43px;display:flex;font-size:11px;color:var(--brown)}
.filters span{padding:5px 14px}
.filters .on{background:var(--brown);color:var(--white)}
.gallery-bg{left:0;top:1826px;width:1200px;height:593px;background:var(--white)}
.tile{position:absolute}
.tile.hl{background:rgba(58,47,38,.92);text-align:center;color:var(--white)}
.tile.hl h5{font-size:15px;font-weight:600;margin-top:140px}
.tile.hl p{font-size:10px}
.tile.hl .plus{color:var(--yellow);font-size:22px;margin-top:8px}

/* suppliers */
.suppliers{left:0;top:2419px;width:1200px;height:438px;background:var(--white);color:var(--ink)}
.sup-head{left:0;width:1200px;top:88px;text-align:center;font-size:17px;font-weight:600;color:var(--brown)}
.sup-head:before,.sup-head:after{content:"";display:inline-block;width:80px;height:1.5px;background:var(--yellow);vertical-align:middle;margin:0 14px}
.sup{width:180px;height:60px;line-height:60px;text-align:center;font-size:22px;font-weight:500;color:#9a9a9a}
.sup.lift{background:var(--white);box-shadow:0 4px 16px rgba(0,0,0,.1)}
.sup-btn{left:543px;top:319px;width:120px;height:34px;line-height:32px;border:1.5px solid var(--ink);font-size:10px;font-weight:600;text-align:center;text-transform:uppercase}

/* careers */
.careers{left:0;top:2857px;width:1200px;height:357px;background:var(--yellow);overflow:hidden}
.careers-photo{left:0;top:0;width:1200px;height:357px;background:linear-gradient(120deg,#c9a36b,#8ea6bf 60%,#d9dee4);clip-path:polygon(714px 0,1200px 0,1200px 357px,607px 357px)}
.careers-copy{left:214px;top:80px}
.careers-copy h2{font-size:28px;font-weight:400;line-height:1.3;color:var(--brown)}
.careers-copy h2 b{color:var(--white);font-weight:600}
.careers-copy p{font-size:12px;color:var(--white);margin-top:14px}
.careers-btn{display:inline-block;margin-top:22px;width:124px;height:34px;line-height:32px;border:1.5px solid var(--brown);color:var(--brown);font-size:10px;font-weight:600;text-align:center;text-transform:uppercase}

/* footer */
.site-footer{left:0;top:3214px;width:1200px;height:357px;background:var(--brown)}
.f-brand{left:83px;top:90px;display:flex;align-items:center;gap:10px}
.f-brand .brand-mark{width:50px;height:50px}
.f-brand .brand-name{font-size:26px}
.f-brand .brand-name small{font-size:12px}
.f-col{top:80px;font-size:11px;line-height:1.75;color:#cfc6bd}
.f-col h6{font-size:13px;font-weight:600;color:var(--white);margin-bottom:12px}
.f-col .phone{font-size:14px;color:var(--white);font-weight:600}
.sub-field{margin-top:10px;width:240px;height:30px;background:var(--brown-dark);display:flex;justify-content:space-between;align-items:center;padding:0 10px;font-size:10px;color:#8a7f75}
.sub-field i{color:var(--yellow);font-style:normal}
.f-rule{left:83px;top:286px;width:1034px;height:1px;background:var(--line)}
.copyright{left:83px;top:307px;font-size:10px;color:#cfc6bd}
.copyright b{color:var(--yellow);font-weight:500}
.f-social{left:1005px;top:300px;display:flex;gap:10px}
.f-social span{width:22px;height:22px;border:1.5px solid var(--yellow);border-radius:50%}
</style>
</head>
<body>

<header class="abs site-header">
  <div class="abs brand"><span class="brand-mark"></span><div class="brand-name">QUARRYBEND<small>BUILDING COMPANY</small></div></div>
  <nav class="abs main-nav"><a class="active">Home</a><a>About</a><a>Divisions</a><a>Gallery</a><a>Supplies</a><a>Career</a></nav>
  <div class="abs header-phone"><svg width="13" height="13" viewBox="0 0 24 24"><path fill="#f5b021" d="M6.6 10.8a15 15 0 0 0 6.6 6.6l2.2-2.2c.3-.3.7-.4 1-.2 1.1.4 2.3.6 3.6.6.6 0 1 .4 1 1V20c0 .6-.4 1-1 1A17 17 0 0 1 3 4c0-.6.4-1 1-1h3.5c.6 0 1 .4 1 1 0 1.3.2 2.5.6 3.6.1.3 0 .7-.2 1z"/></svg>555-014-2290</div>
  <a class="abs btn header-cta">Contact Us</a>
</header>

<section>
  <div class="abs hero" role="img" aria-label="Low-angle view of high-rise towers under construction with tower cranes against a cloudy sky"></div>
  <div class="abs social-rail"><span></span><span></span><span></span><span></span></div>
  <h1 class="abs hero-title"><b>Quarrybend</b> is a Innovation<br>Construction</h1>
  <a class="abs btn hero-cta">Explore More</a>
</section>

<section>
  <div class="abs about-photo" role="img" aria-label="Modern living room interior with fireplace, wood panel wall and sofa"></div>
  <div class="abs about-body">
    <h2>Contrary to popular<br>Lorem Ipsum</h2>
    <h3>There are many variations of passages of Lorem Ipsum available lorem</h3>
    <p>Contrary to popular belief, Lorem Ipsum is not simply random work random text. It has roots in a piece of classical Latin literature from 45 BC, making it over 2000 years old. Henry Alderwood, a Latin professor at Ashford Hill College in Virginia...</p>
    <a class="link-more">Discover More →</a>
  </div>
  <div class="abs stat" style="left:212px">
    <svg viewBox="0 0 105 105"><circle cx="52.5" cy="52.5" r="50" fill="none" stroke="#5a4d41" stroke-width="2"/><circle cx="52.5" cy="52.5" r="50" fill="none" stroke="#f5b021" stroke-width="2" stroke-dasharray="110 314" transform="rotate(-90 52.5 52.5)"/><text x="52.5" y="61" text-anchor="middle" fill="#f5b021" font-family="Poppins,sans-serif" font-size="26">35%</text></svg>
    <div><div class="cap">Projects</div><div class="name">Codes</div><div class="desc">Lorem ipsum dolor sit<br>amet message</div></div>
  </div>
  <div class="abs stat" style="left:477px">
    <svg viewBox="0 0 105 105"><circle cx="52.5" cy="52.5" r="50" fill="none" stroke="#5a4d41" stroke-width="2"/><circle cx="52.5" cy="52.5" r="50" fill="none" stroke="#f5b021" stroke-width="2" stroke-dasharray="236 314" transform="rotate(-90 52.5 52.5)"/><text x="52.5" y="61" text-anchor="middle" fill="#f5b021" font-family="Poppins,sans-serif" font-size="26">75%</text></svg>
    <div><div class="cap">Happy</div><div class="name">Clients</div><div class="desc">Lorem ipsum dolor sit<br>amet message</div></div>
  </div>
  <div class="abs stat" style="left:741px">
    <svg viewBox="0 0 105 105"><circle cx="52.5" cy="52.5" r="50" fill="none" stroke="#5a4d41" stroke-width="2"/><circle cx="52.5" cy="52.5" r="50" fill="none" stroke="#f5b021" stroke-width="2" stroke-dasharray="214 314" transform="rotate(-90 52.5 52.5)"/><text x="52.5" y="61" text-anchor="middle" fill="#f5b021" font-family="Poppins,sans-serif" font-size="26">68%</text></svg>
    <div><div class="cap">Completed</div><div class="name">Projects</div><div class="desc">Lorem ipsum dolor sit<br>amet message</div></div>
  </div>
</section>

<section class="abs services">
  <h2 class="abs section-title" style="left:214px;top:82px">Our Services</h2>
  <a class="abs view-all" style="left:926px;top:96px">View All →</a>
  <span class="abs arrow" style="left:144px;top:278px">‹</span>
  <span class="abs arrow" style="left:1046px;top:278px">›</span>
  <div class="abs service-card" style="left:214px;padding-top:20px">
    <svg width="44" height="44" viewBox="0 0 44 44" fill="none" stroke="#f5b021" stroke-width="2"><path d="M4 22 22 6l18 16"/><path d="M9 18v20h26V18"/><rect x="18" y="26" width="8" height="12"/></svg>
    <h4>Residential</h4>
    <p>Contrary to popular belief, Lorem Ipsum is not simply random text. It has roots in a piece of classical Latin literature from 45 BC, making it over...</p>
    <a class="read">Read More →</a>
  </div>
  <div class="abs service-card" style="left:479px;padding-top:20px">
    <svg width="44" height="44" viewBox="0 0 44 44" fill="none" stroke="#f5b021" stroke-width="2"><rect x="8" y="12" width="28" height="28"/><path d="M14 12V6h16v6"/><path d="M14 20h4M26 20h4M14 28h4M26 28h4"/><rect x="19" y="32" width="6" height="8"/></svg>
    <h4>Commercial</h4>
    <p>Contrary to popular belief, Lorem Ipsum is not simply random text. It has roots in a piece of classical Latin literature from 45 BC, making it over...</p>
    <a class="read">Read More →</a>
  </div>
  <div class="abs service-card featured" style="left:743px">
    <svg width="44" height="44" viewBox="0 0 44 44" fill="none" stroke="#ffffff" stroke-width="2"><path d="M4 40V22l10 6v-6l10 6v-6l10 6V8h6v32z"/><path d="M4 40h36"/></svg>
    <h4>Industrial</h4>
    <p>Contrary to popular belief, Lorem Ipsum is not simply random text. It has roots in a piece of classical Latin literature from 45 BC, making it over...</p>
    <a class="read">Read More →</a>
  </div>
</section>

<section>
  <div class="abs gallery-band">
    <h2 class="section-title">Projects Gallery</h2>
    <div class="abs filters"><span class="on">All</span><span>Residential</span><span>Commercial</span><span>Industrial</span></div>
  </div>
  <div class="abs gallery-bg">
    <div class="tile" style="left:0;top:22px;width:588px;height:273px;background:linear-gradient(180deg,#5e9be0,#b6cfe8 60%,#8a8f98)" role="img" aria-label="Tower cranes over a building site under a blue sky"></div>
    <div class="tile hl" style="left:612px;top:22px;width:283px;height:273px"><h5>Construction Build</h5><p>Contrary to popular</p><div class="plus">+</div></div>
    <div class="tile" style="left:917px;top:22px;width:283px;height:273px;background:linear-gradient(180deg,#7fb4e6,#d9c7a3 65%,#8a6a48)" role="img" aria-label="Crane above a concrete frame at golden hour"></div>
    <div class="tile" style="left:0;top:319px;width:283px;height:274px;background:linear-gradient(180deg,#e89a3c,#6c3d22 70%,#2d1a12)" role="img" aria-label="Workers silhouetted on rebar against a sunset"></div>
    <div class="tile" style="left:305px;top:319px;width:283px;height:274px;background:linear-gradient(180deg,#3f86d4,#9cc3e8 55%,#b08a5c)" role="img" aria-label="Excavator working on a dirt site under a blue sky"></div>
    <div class="tile" style="left:612px;top:319px;width:588px;height:274px;background:linear-gradient(180deg,#e2b878,#9a7454 55%,#4a3a2e)" role="img" aria-label="Workers tying rebar on a concrete deck at dusk"></div>
  </div>
</section>

<section class="abs suppliers">
  <h2 class="abs sup-head">Supplier</h2>
  <div class="abs sup" style="left:220px;top:143px">NORVIK</div>
  <div class="abs sup lift" style="left:412px;top:143px">Beltane</div>
  <div class="abs sup" style="left:605px;top:143px">Oskar</div>
  <div class="abs sup" style="left:800px;top:143px">Tidewell</div>
  <div class="abs sup" style="left:220px;top:218px">Marrow</div>
  <div class="abs sup" style="left:412px;top:218px">Fenrow</div>
  <div class="abs sup" style="left:605px;top:218px">Calder</div>
  <div class="abs sup" style="left:800px;top:218px">Lumo</div>
  <a class="abs sup-btn">View All</a>
</section>

<section class="abs careers">
  <div class="abs careers-photo" role="img" aria-label="Smiling construction workers in hard hats in front of a building site"></div>
  <div class="abs careers-copy">
    <h2>If you find a Lorem Ipsum<br><b>Secure Job</b> For Your<br>Carrier?</h2>
    <p>Contrary to popular belief, Lorem Ipsum</p>
    <a class="careers-btn">Find Your Job</a>
  </div>
</section>

<footer class="abs site-footer">
  <div class="abs f-brand"><span class="brand-mark"></span><div class="brand-name">QUARRYBEND<small>BUILDING COMPANY</small></div></div>
  <div class="abs f-col" style="left:433px">
    <h6>Contact Us</h6>
    <div>Call: <span class="phone">555-014-2290</span></div>
    <div>E: info@quarrybend.com</div>
    <div style="margin-top:10px;color:#fff">Address:</div>
    <div>48 Ridgefield Avenue,<br>Eastvale, QB 20418</div>
  </div>
  <div class="abs f-col" style="left:698px">
    <h6>Quick Links</h6>
    <div>About</div><div>Divisions</div><div>Gallery</div><div>Supplies</div><div>Career</div><div>Contact</div>
  </div>
  <div class="abs f-col" style="left:874px">
    <h6>Subscribe Now!</h6>
    <div>You Want to get Update<br>about anything News? Join Me Now!</div>
    <div class="sub-field">Enter Your Email...<i>➤</i></div>
  </div>
  <div class="abs f-rule"></div>
  <div class="abs copyright">© 2019 <b>Quarrybend Building Company</b>. All Right Reserved</div>
  <div class="abs f-social"><span></span><span></span><span></span><span></span></div>
</footer>

</body>
</html>
```